Luxury Tea Brand Needs Packaging Design

Our team needs a luxe design replicating the shape of the attached picture for a box that will contain drawstring teabags. There is an opportunity for silver or gold reflective design

Please include a design for the

Product dimensions - 10.5x4x9 cm
things to keep in mind

- luxury design
- Mainly black with either silver or gold
- Should say pack of 100
- Should say Leaf Harbor Tea Filters

some of our products have been attached as a style reference

website is www.leafharbor.example

Target Market(s)

modern millennials

Requirements
Must have
• luxury feel
Nice to have
• shiny designs

```html
<!DOCTYPE html>
<html lang="en">
<head>
<meta charset="UTF-8">
<title>Leaf Harbor Tea Filters – Box Front</title>
<link rel="stylesheet" href="https://fonts.googleapis.com/css2?family=Cinzel:wght@400;500&display=swap">
<style>
  :root {
    --box-black: #000000;
    --silver-light: #e4e4e4;
    --silver-mid: #a9a9a9;
    --silver-dark: #5a5a5a;
    --label-white: #f2f2f2;
  }
  html, body {
    margin: 0;
    padding: 0;
    width: 1028px;
    height: 1200px;
    overflow: hidden;
    background: var(--box-black);
  }
  .box-front {
    position: relative;
    width: 1028px;
    height: 1200px;
    background: var(--box-black);
    font-family: "Cinzel", "Times New Roman", serif;
    overflow: hidden;
  }
  .leaf-mandala {
    position: absolute;
    left: 70px;
    top: -20px;
    width: 888px;
    height: 500px;
    border-radius: 0 0 444px 444px / 0 0 500px 500px;
    background: radial-gradient(ellipse at 50% 0%,
      rgba(200,200,200,0.05) 0%,
      rgba(200,200,200,0.28) 45%,
      rgba(170,170,170,0.38) 70%,
      rgba(90,90,90,0.18) 90%,
      rgba(0,0,0,0) 100%);
  }
  .brand-frame {
    position: absolute;
    left: 251px;
    top: 522px;
    width: 541px;
    height: 309px;
    box-sizing: border-box;
    border: 5px solid var(--silver-mid);
    border-image: linear-gradient(135deg, var(--silver-light), var(--silver-dark) 50%, var(--silver-light)) 1;
    display: flex;
    align-items: center;
    justify-content: center;
  }
  .brand-name {
    margin: 0;
    color: var(--silver-light);
    font-weight: 400;
    font-size: 66px;
    letter-spacing: 2px;
    line-height: 1;
  }
  .product-name {
    position: absolute;
    left: 0;
    width: 100%;
    top: 996px;
    margin: 0;
    text-align: center;
    color: var(--label-white);
    font-weight: 400;
    font-size: 36px;
    letter-spacing: 10px;
  }
  .pack-count {
    position: absolute;
    left: 0;
    width: 100%;
    top: 1092px;
    margin: 0;
    text-align: center;
    color: var(--label-white);
    font-weight: 400;
    font-size: 22px;
    letter-spacing: 5px;
  }
</style>
</head>
<body>
  <main class="box-front">
    <div class="leaf-mandala" role="img" aria-label="Silver half-mandala ornament of tea leaves and dots"></div>
    <div class="brand-frame">
      <h1 class="brand-name">Leaf Harbor</h1>
    </div>
    <p class="product-name">TEA FILTERS</p>
    <p class="pack-count">BOX OF 100</p>
  </main>
</body>
</html>
```